Capability Statement Brochure - Corporate

We need to provide our corporate clients with an elegant, professional and well designed capability statement that not only details what our business can offer, but reflects our professionalism with relevant technical photos. I am thinking two pages A 4 pdf will be suitable if the text can fit without looking crowded but happy to extend to 3 or 4 pages if needed . Colours and details can be taken from our website www.kelvorapro.com.au Some photos have been attached however if we need more professional stock photos I am happy to use them if needed. This project needs to convince potential clients we are the best in industry and our capability is extensive. Please help us relay this to our customers. Thank you,.

Target Market(s)

Corporate, Government, Education, Defence, Healthcare

Industry/Entity Type

Audio Visual Integration

Colors
0054AA
0677BA
7BADD7
CADEEF
E8F1F8

Requirements
Must have
• Style, look classy, sophisticated and technical
Nice to have
• Kelvora colours, Logo, website and email and include the TARNIX LED Logo
Should not have
• Messy, too much clutter, not easy to read.

```html
<!DOCTYPE html>
<html lang="en">
<head>
<meta charset="utf-8">
<title>Kelvora Systems – Capability Statement</title>
<link href="https://fonts.googleapis.com/css2?family=Poppins:wght@400;500;600;700;800&display=swap" rel="stylesheet">
<style>
:root{
  --blue:#2c57b3;
  --blue-deep:#0054aa;
  --blue-mid:#0677ba;
  --blue-light:#7badd7;
  --blue-pale:#cadeef;
  --orange:#f39325;
  --panel:#ececec;
  --ink:#2a2a2a;
  --stage:#d6d6d6;
  --white:#ffffff;
}
*{margin:0;padding:0;box-sizing:border-box}
html,body{width:858px;height:1200px;overflow:hidden;background:var(--stage);font-family:'Poppins',sans-serif;color:var(--ink)}
.canvas{position:relative;width:858px;height:1200px}
.page{position:absolute;width:363px;height:470px;background:var(--white);overflow:hidden;transform:scale(.858);transform-origin:0 0}
.page--cover{left:77px;top:131px}
.page--back{left:459px;top:131px}
.page--overview{left:77px;top:646px}
.page--sectors{left:459px;top:646px}
.abs{position:absolute}
.photo{position:absolute}
.brand{position:absolute;display:flex;align-items:center;gap:5px;font-weight:600;color:var(--ink);white-space:nowrap}
.brand__dot{width:12px;height:12px;background:var(--blue)}
.product{position:absolute;font-weight:800;letter-spacing:.5px;white-space:nowrap}
p,li{font-size:4.4px;line-height:1.45}
/* cover */
.cover__title{position:absolute;left:35px;top:346px;font-weight:800;font-size:29px;line-height:1.05;color:var(--white)}
.cover__title span{display:block;color:var(--blue-light)}
.cover__url{position:absolute;left:35px;top:414px;width:163px;height:15px;border-radius:8px;background:var(--blue);color:var(--white);font-size:7.5px;text-align:center;line-height:15px}
/* back */
.why{position:absolute;left:18px;top:18px;width:327px;height:150px;background:var(--panel);border-radius:9px}
.why__tab{position:absolute;left:50%;top:-4px;transform:translateX(-50%);background:var(--orange);color:var(--white);font-size:6.2px;font-weight:600;padding:2px 12px;border-radius:0 0 8px 8px;white-space:nowrap}
.ticks{position:absolute;list-style:none;width:140px}
.ticks li{position:relative;padding-left:8px;margin-bottom:3.4px}
.ticks li::before{content:"";position:absolute;left:0;top:1px;width:4.5px;height:4.5px;background:var(--orange);border-radius:1px}
.contact__head{position:absolute;left:0;right:0;top:392px;display:flex;align-items:center;justify-content:center;gap:8px;color:var(--blue);font-size:9.5px;font-weight:500}
.contact__head i{display:block;width:45px;height:1px;background:var(--blue)}
.contact__row{position:absolute;left:0;right:0;top:412px;display:flex;justify-content:center;gap:10px;font-size:5.6px;font-weight:500;color:var(--ink)}
.contact__row span{display:flex;align-items:center;gap:3px}
.contact__row svg{width:8px;height:8px}
/* overview */
.h2{position:absolute;font-weight:700;font-size:13.5px;color:var(--blue);white-space:nowrap}
.h2--light{color:var(--white)}
.copy{position:absolute;color:var(--ink)}
.copy--light{color:var(--white)}
.copy p{margin-bottom:3px}
.caps{position:absolute;left:17px;top:124px;width:328px;height:148px;background:var(--panel);border-radius:9px}
.caps__grid{position:absolute;left:14px;top:32px;width:300px;display:grid;grid-template-columns:1fr 1fr;row-gap:9px;column-gap:10px}
.cap{display:flex;align-items:center;gap:5px;font-size:4.5px;line-height:1.3;height:14px}
.cap i{flex:none;width:12px;height:12px;border-radius:50%;background:var(--blue);border:1.5px solid var(--blue-pale)}
.cap i.o{background:var(--orange);border-color:#fbd4a6}
.markets{position:absolute;list-style:none;width:60px}
.markets li{position:relative;padding-left:6px;margin-bottom:1px}
.markets li::before{content:"";position:absolute;left:0;top:1.5px;width:3px;height:3px;background:var(--orange)}
.foot{position:absolute;left:30px;top:447px;font-size:5px;color:var(--ink)}
.pg{position:absolute;right:26px;top:446px;width:28px;height:8px;border-radius:4px;background:var(--blue);color:var(--white);font-size:4.5px;text-align:center;line-height:8px;font-weight:600}
/* sectors */
.sector{position:absolute;width:150px}
.pill{display:flex;align-items:center;height:13px;background:var(--blue);border-radius:7px;color:var(--white);font-size:6.4px;font-weight:500;padding-left:3px;gap:5px;margin-bottom:5px;width:142px}
.pill i{flex:none;width:11px;height:11px;border-radius:50%;background:var(--orange);border:1.5px solid var(--white)}
.pill--alt i{background:var(--blue);}
.sector p{color:var(--ink);padding-left:2px;width:140px;margin-bottom:3px}
.band{position:absolute;left:0;top:360px;width:363px;height:110px;background:var(--orange)}
.band .sector p{color:var(--white)}
.band .foot{top:87px;left:18px;color:var(--white)}
.band .pg{top:86px;background:var(--white);color:var(--orange)}
</style>
</head>
<body>
<div class="canvas">

  <!-- Page: cover -->
  <section class="page page--cover">
    <svg class="abs" style="left:0;top:0" width="363" height="470" viewBox="0 0 363 470">
      <polygon points="0,0 158,0 104,72 0,72" fill="#2c57b3"/>
      <polygon points="163,0 178,0 124,72 109,72" fill="#7badd7"/>
      <polygon points="363,352 363,455 300,455" fill="#2c57b3"/>
      <polygon points="363,420 363,455 335,455" fill="#7badd7"/>
    </svg>
    <div class="brand" style="left:232px;top:26px;font-size:11px"><span class="brand__dot"></span>kelvora systems</div>
    <div class="photo" role="img" aria-label="Photo of a meeting room with a person presenting at a wall display above a conference table" style="left:20px;top:72px;width:323px;height:376px;background:linear-gradient(180deg,#a88a6a 0%,#6d5845 35%,#3a3532 60%,#262525 100%)"></div>
    <h1 class="cover__title"><span>CAPABILITY</span>STATEMENT</h1>
    <div class="cover__url">www.kelvorapro.com.au</div>
    <div class="product" style="left:236px;top:416px;font-size:11px;color:var(--white)">TARNIX LED</div>
  </section>

  <!-- Page: back cover -->
  <section class="page page--back">
    <div class="abs" style="left:0;top:0;width:363px;height:200px;background:var(--blue)"></div>
    <div class="why">
      <div class="why__tab">Why Choose Kelvora Systems</div>
      <ul class="ticks" style="left:14px;top:24px">
        <li>25+ years of proven industry experience.</li>
        <li>End-to-end capability from consultation, design, installation and support.</li>
        <li>Specialisation in LED &amp; large-scale displays, LED video walls, digital signage and high-impact visual environments.</li>
        <li>Tailored solutions to suit your unique operational needs and goals.</li>
        <li>Trusted by major organisations including healthcare, education, government and enterprise sectors.</li>
        <li>National coverage with ability to deliver and support projects across metropolitan and regional Australia.</li>
      </ul>
      <ul class="ticks" style="left:175px;top:24px">
        <li>Highly skilled technical team of experienced engineers, programmers and technicians.</li>
        <li>Our solutions are designed to be simple and intuitive, minimising training requirements and user frustration.</li>
        <li>Seamless integration with leading meeting platforms, unified communications and enterprise IT environments.</li>
        <li>We have strong partnerships with leading global AV manufacturers to ensure performance, longevity and supportability.</li>
        <li>Ongoing support &amp; maintenance with long-term client relationships in mind, not just a one-off install.</li>
        <li>Reputation for delivery &amp; reliability.</li>
      </ul>
    </div>
    <svg class="abs" style="left:0;top:0" width="363" height="470" viewBox="0 0 363 470">
      <polygon points="363,180 363,228 262,352 224,352" fill="#2c57b3"/>
      <polygon points="363,250 363,290 315,352 285,352" fill="#7badd7"/>
    </svg>
    <div class="photo" role="img" aria-label="Photo of a large LED video wall showing a city skyline in a brick sports hall" style="left:28px;top:180px;width:290px;height:173px;background:linear-gradient(135deg,#9a6a45 0%,#7c5236 50%,#5b3d2a 100%)"></div>
    <div class="brand" style="left:126px;top:364px;font-size:8.5px"><span class="brand__dot" style="width:10px;height:10px"></span>kelvora systems</div>
    <div class="contact__head"><i></i>CONTACT US<i></i></div>
    <div class="contact__row">
      <span><svg viewBox="0 0 10 10"><circle cx="5" cy="5" r="5" fill="#2c57b3"/><path d="M3.3 2.6l1 1-.5.7c.4.8 1 1.4 1.9 1.9l.7-.5 1 1-.7.8C4.7 7.3 2.7 5.3 2.5 3.3z" fill="#fff"/></svg>1300 555 019 (NATIONAL)</span>
      <span><svg viewBox="0 0 10 10"><circle cx="5" cy="5" r="5" fill="#2c57b3"/><rect x="2.5" y="3.2" width="5" height="3.6" fill="none" stroke="#fff" stroke-width=".7"/><path d="M2.5 3.2l2.5 2 2.5-2" fill="none" stroke="#fff" stroke-width=".7"/></svg>info@kelvorapro.com.au</span>
      <span><svg viewBox="0 0 10 10"><circle cx="5" cy="5" r="5" fill="#2c57b3"/><circle cx="5" cy="5" r="2.6" fill="none" stroke="#fff" stroke-width=".7"/><path d="M2.4 5h5.2M5 2.4v5.2" stroke="#fff" stroke-width=".6"/></svg>www.kelvorapro.com.au</span>
    </div>
    <div class="product" style="left:0;right:0;top:430px;text-align:center;font-size:11px;color:var(--ink)">TARNIX LED</div>
  </section>

  <!-- Page: company overview -->
  <section class="page page--overview">
    <div class="abs" style="left:0;top:0;width:363px;height:165px;background:var(--blue)"></div>
    <h2 class="h2 h2--light" style="left:30px;top:16px">Company Overview</h2>
    <div class="copy copy--light" style="left:30px;top:42px;width:302px">
      <p>Kelvora Systems (KMS) is a leading Australian audiovisual integration specialist delivering advanced AV, unified communications, collaboration environments and large-scale digital display systems across Australia.</p>
      <p>With more than 25 years of industry experience, KMS provides end-to-end services including system design, engineering, installation, commissioning and long term technical support. Our solutions enable organisations to communicate, collaborate and share information effectively across boardrooms, control centres, training environments, operational facilities and large public spaces.</p>
      <p>KMS works across a broad range of sectors including healthcare, corporate enterprise, government, defence, mining and resources, and education. Our team combines deep technical expertise with a strong understanding of operational environments where reliability, security and ease of use are essential.</p>
    </div>
    <div class="caps">
      <h2 class="h2" style="left:17px;top:6px">Core Capabilities</h2>
      <div class="caps__grid">
        <div class="cap"><i></i>AV System Design and Engineering</div>
        <div class="cap"><i class="o"></i>Education and Training Environments</div>
        <div class="cap"><i class="o"></i>Unified Communications and<br>Collaboration Systems</div>
        <div class="cap"><i></i>Digital Signage and Information Display Networks</div>
        <div class="cap"><i></i>LED Video Walls and Large Format Displays</div>
        <div class="cap"><i class="o"></i>AV over IP and Networked Media Systems</div>
        <div class="cap"><i class="o"></i>Control Rooms and Operations Centres</div>
        <div class="cap"><i></i>System Programming, Automation<br>and Control</div>
        <div class="cap"><i></i>Boardrooms and Executive Meeting Spaces</div>
        <div class="cap"><i class="o"></i>Ongoing Service, Maintenance and<br>Technical Support</div>
      </div>
    </div>
    <h2 class="h2" style="left:30px;top:284px">LED Video Wall Expertise</h2>
    <div class="copy" style="left:30px;top:306px;width:302px">
      <p>Kelvora Systems has extensive experience designing and installing direct view LED video walls for corporate environments, education facilities, public venues and large presentation spaces.</p>
      <p>Our proprietary TARNIX LED video wall solutions provide exceptional brightness, durability and reliability for high-impact display environments such as school halls, gymnasiums, corporate auditoriums and public venues.</p>
      <p>KMS provides complete LED video wall solutions including structural design, engineering certification, installation, commissioning and ongoing support.</p>
    </div>
    <h2 class="h2" style="left:30px;top:370px">Markets Served</h2>
    <ul class="markets" style="left:30px;top:396px">
      <li>Healthcare</li><li>Corporate<br>&amp; Enterprise</li><li>Government</li><li>Defence</li>
    </ul>
    <ul class="markets" style="left:94px;top:396px">
      <li>Mining &amp; Resources</li><li>Education</li><li>Public Venues &amp;<br>Event Spaces</li>
    </ul>
    <div class="photo" role="img" aria-label="Photo of an operator at a control room desk in front of a wall of monitoring screens" style="left:180px;top:373px;width:157px;height:67px;background:linear-gradient(160deg,#5b7fae 0%,#2d3e5c 55%,#1b2433 100%)"></div>
    <div class="foot">www.kelvorapro.com.au</div>
    <div class="pg">PG-1</div>
  </section>

  <!-- Page: sectors and services -->
  <section class="page page--sectors">
    <div class="sector" style="left:17px;top:18px">
      <div class="pill"><i></i>Healthcare Experience</div>
      <p>KMS has extensive experience delivering audiovisual solutions within major healthcare environments including clinical communication systems, specialist consultation rooms, training facilities and hospital-wide digital signage networks. For over 20 years KMS has supported hospitals and medical providers with design, implementation and support of audiovisual infrastructure across departments including ICU, Emergency, Cardiology, Radiology and Allied Health.</p>
    </div>
    <div class="sector" style="left:17px;top:112px">
      <div class="pill"><i></i>Education</div>
      <p>KMS delivers innovative AV solutions for schools, universities and training institutions including lecture theatres, classrooms, hybrid learning environments, school halls, gymnasiums and large-scale LED display systems.</p>
    </div>
    <div class="sector" style="left:17px;top:183px">
      <div class="pill"><i></i>Design &amp; Engineering</div>
      <p>KMS provides comprehensive in-house design and engineering services including system architecture, documentation, schematics, networked AV design and integration with existing IT infrastructure. Our team works closely with architects, consultants, builders and project managers to ensure seamless integration of audiovisual technology within new builds and refurbishment projects.</p>
    </div>
    <div class="sector" style="left:17px;top:271px">
      <div class="pill"><i></i>Implementation &amp; Commissioning</div>
      <p>KMS delivers complete turnkey project implementation including equipment procurement, professional installation, system configuration, testing, commissioning and user training. Our accredited technicians ensure systems are delivered safely, efficiently and with minimal disruption to operational environments.</p>
    </div>
    <div class="sector" style="left:180px;top:18px">
      <div class="pill"><i></i>Corporate &amp; Enterprise</div>
      <p>KMS delivers modern collaboration environments that enable organisations to connect teams across offices, remote staff and global partners.</p>
      <p>Solutions include boardrooms, hybrid meeting rooms, training facilities, corporate digital signage networks and executive collaboration spaces.</p>
    </div>
    <div class="sector" style="left:180px;top:106px">
      <div class="pill"><i></i>Mining &amp; Resources</div>
      <p>KMS provides robust AV systems designed for industrial and remote environments including operations centres, training rooms, induction facilities and remote collaboration systems supporting mining and energy sector operations.</p>
    </div>
    <div class="sector" style="left:180px;top:176px">
      <div class="pill"><i></i>Government &amp; Defence</div>
      <p>KMS supports government departments and defence organisations with reliable and secure audiovisual systems designed for operational environments including command centres, training facilities, situation rooms and secure conferencing spaces.</p>
    </div>
    <div class="photo" role="img" aria-label="Photo of a boardroom with a long table facing a row of wall-mounted displays" style="left:182px;top:247px;width:163px;height:93px;background:linear-gradient(180deg,#3c4f6e 0%,#7c8796 45%,#b9a89a 100%)"></div>
    <div class="band">
      <div class="sector" style="left:17px;top:8px">
        <div class="pill pill--alt"><i></i>Service &amp; Support</div>
        <p>KMS provides comprehensive ongoing support services including preventative maintenance, priority service response, remote diagnostics, system upgrades and technology lifecycle planning. Our long-term support partnerships ensure systems remain reliable, secure and aligned with evolving organisational needs.</p>
      </div>
      <div class="sector" style="left:180px;top:8px">
        <div class="pill pill--alt"><i></i>Governance, Safety &amp; Compliance</div>
        <p>KMS operates under strict safety and governance frameworks including OH&amp;S compliant work practices, industry-certified technicians and full public liability and professional indemnity coverage. Safety, compliance and quality assurance are embedded throughout all project delivery activities.</p>
      </div>
      <div class="foot">www.kelvorapro.com.au</div>
      <div class="pg">PG-2</div>
    </div>
  </section>

</div>
</body>
</html>
```